Business Card for Mortuary

We need a business card design for our mortuary. We are not the "traditional" mortuary and specialize in simple cremations and burials. We use a two sided card.

Industry/Entity Type

Funeral Home

Contact Information for Business Card

One side we would like to have with the general information of the mortuary:
Address: 4127 E. Larkspur Ave, Sun City, AZ 85399
Phone: 623-555-0142
email: hello@willowbendmortuary.example
website: willowbendmortuary.example

On the other side would like to have the information of employee:
Name: Mark T. Ellis
Email: mark@willowbendmortuary.example
Title: Funeral Director
Text: 602-555-0187

Font styles to use
Serif
Sans Serif

Requirements
Should not have
• Do not put any gothic images or things like a hearse or tombstone.

```html
<!DOCTYPE html>
<html lang="en">
<head>
<meta charset="utf-8">
<title>Willowbend Mortuary – Business Card</title>
<link rel="stylesheet" href="https://fonts.googleapis.com/css2?family=Arimo:wght@400;700&family=Source+Sans+3:wght@400;600;700&display=swap">
<style>
  :root {
    --stage: #e6e6e6;
    --card-dark: #0a0a0a;
    --card-light: #f4f4f4;
    --green: #8dc63f;
    --green-deep: #6cb33f;
    --white: #ffffff;
    --ink: #1a1a1a;
  }
  * { box-sizing: border-box; margin: 0; padding: 0; }
  html, body { width: 1200px; height: 960px; overflow: hidden; }
  body {
    background: var(--stage);
    position: relative;
    font-family: "Source Sans 3", Arial, sans-serif;
  }
  .card {
    position: absolute;
    left: 316px;
    width: 569px;
    height: 325px;
    overflow: hidden;
  }
  .card--front { top: 130px; background: var(--card-dark); }
  .card--back { top: 505px; background: var(--card-light); }

  /* Front */
  .brand-row {
    position: absolute;
    top: 126px;
    left: 0; right: 0;
    display: flex;
    justify-content: center;
    align-items: center;
    gap: 10px;
  }
  .brand-dot {
    width: 16px; height: 16px;
    border-radius: 50%;
    background: var(--green);
  }
  .brand-name {
    font-family: "Arimo", Arial, sans-serif;
    font-weight: 700;
    color: var(--white);
    font-size: 27px;
    line-height: 30px;
    letter-spacing: -0.3px;
  }
  .brand-divider {
    width: 2px; height: 64px;
    background: var(--green);
    margin-left: 4px;
  }
  .tagline {
    font-family: "Arimo", Arial, sans-serif;
    color: var(--green);
    font-size: 17.5px;
    line-height: 22px;
  }
  .front-contact {
    position: absolute;
    top: 230px; left: 0; right: 0;
    text-align: center;
    color: var(--white);
    font-size: 14px;
    line-height: 18px;
  }
  .front-contact .row { display: flex; justify-content: center; align-items: center; gap: 14px; }
  .front-contact .item { display: inline-flex; align-items: center; gap: 3px; }
  .icon { width: 13px; height: 13px; fill: var(--green); }
  .web-rule {
    position: absolute;
    top: 281px; left: 44px; right: 44px;
    display: flex; align-items: center; gap: 10px;
  }
  .web-rule .line { flex: 1; height: 2px; background: var(--green); }
  .web-rule .url {
    color: var(--green);
    font-weight: 700;
    font-size: 14px;
    letter-spacing: 1px;
  }

  /* Back */
  .back-panel { position: absolute; left: 0; top: 0; width: 240px; height: 325px; }
  .back-brand { position: absolute; left: 31px; top: 33px; }
  .back-brand .brand-name { font-size: 21px; line-height: 22px; }
  .back-brand .tagline { margin-top: 22px; font-size: 15.5px; line-height: 19px; }
  .person {
    position: absolute;
    right: 34px; top: 178px;
    text-align: right;
  }
  .person-name { color: var(--green); font-weight: 700; font-size: 20px; letter-spacing: 0.6px; line-height: 24px; }
  .person-title { color: var(--ink); font-size: 14px; line-height: 18px; }
  .person-contact {
    position: absolute;
    right: 32px; top: 254px;
    color: var(--ink);
    font-size: 14px;
    line-height: 19px;
    text-align: right;
  }
  .person-contact .item { display: flex; justify-content: flex-end; align-items: center; gap: 6px; }
</style>
</head>
<body>

<section class="card card--front" aria-label="Business card front">
  <div class="brand-row">
    <span class="brand-dot" aria-hidden="true"></span>
    <div class="brand-name">WILLOWBEND<br>MORTUARY</div>
    <span class="brand-divider" aria-hidden="true"></span>
    <div class="tagline">Affordable<br>Cremation<br>and Burial</div>
  </div>

  <div class="front-contact">
    <div>4127 E. Larkspur Ave, Sun City, AZ 85399</div>
    <div class="row">
      <span class="item">
        <svg class="icon" viewBox="0 0 24 24" aria-hidden="true"><path d="M6.6 10.8a15.1 15.1 0 0 0 6.6 6.6l2.2-2.2c.3-.3.7-.4 1-.2 1.1.4 2.3.6 3.6.6.6 0 1 .4 1 1V20c0 .6-.4 1-1 1A17 17 0 0 1 3 4c0-.6.4-1 1-1h3.5c.6 0 1 .4 1 1 0 1.3.2 2.5.6 3.6.1.3 0 .7-.2 1z"/></svg>
        623-555-0142
      </span>
      <span class="item">
        <svg class="icon" viewBox="0 0 24 24" aria-hidden="true"><path d="M2 5h20v14H2zm2 2v.4l8 5.2 8-5.2V7zm0 2.8V17h16V9.8l-8 5.2z"/></svg>
        hello@willowbendmortuary.example
      </span>
    </div>
  </div>

  <div class="web-rule">
    <span class="line"></span>
    <span class="url">willowbendmortuary.example</span>
    <span class="line"></span>
  </div>
</section>

<section class="card card--back" aria-label="Business card back">
  <svg class="back-panel" viewBox="0 0 240 325" aria-hidden="true">
    <path d="M0 0H211C160 70 128 150 150 225C168 285 150 315 128 325H0Z" fill="#0a0a0a"/>
  </svg>

  <div class="back-brand">
    <div class="brand-name">WILLOWBEND<br>MORTUARY</div>
    <div class="tagline">Affordable<br>Cremation<br>and Burial</div>
  </div>

  <div class="person">
    <div class="person-name">MARK T. ELLIS</div>
    <div class="person-title">Funeral Director</div>
  </div>

  <div class="person-contact">
    <div class="item">602-555-0187
      <svg class="icon" viewBox="0 0 24 24" aria-hidden="true"><path d="M7 1h10a2 2 0 0 1 2 2v18a2 2 0 0 1-2 2H7a2 2 0 0 1-2-2V3a2 2 0 0 1 2-2zm0 3v14h10V4zm5 15.5a1 1 0 1 0 0 2 1 1 0 0 0 0-2z"/></svg>
    </div>
    <div class="item">mark@willowbendmortuary.example
      <svg class="icon" viewBox="0 0 24 24" aria-hidden="true"><path d="M2 5h20v14H2zm2 2v.4l8 5.2 8-5.2V7zm0 2.8V17h16V9.8l-8 5.2z"/></svg>
    </div>
  </div>
</section>

</body>
</html>
```